Home page concept, possible logo colour change

There is no need to code a home page, we are just looking for concept ideas.
We have had a logo designed for a new company we are starting named Corvantek Aluminium Windows & Doors. We are manufacturing bullet resistant window frames. We have had logo designed, we like the concept of the design, but the current colours (black and red) may not be the best option, especially when designing the website home page, and how it interacts with the logo colours. I have also attached the first draft of the home page which we are not happy with. The overall design/navigation is good, we have issues with the darkened out primary image and also the amount of red on the page, it just doesn't feel right. As mentioned before we are happy to look at colour changes to the logo.
Number of Pages Required
1 page
Look and feel
Each slider illustrates characteristics of the customer's brand and the style your logo design should communicate.

```html
<!DOCTYPE html>
<html lang="en">
<head>
<meta charset="utf-8">
<title>Corvantek Aluminium Windows &amp; Doors</title>
<link href="https://fonts.googleapis.com/css2?family=Inter:wght@400;500;600;700;800&display=swap" rel="stylesheet">
<style>
:root{
  --navy:#0b4a8a;
  --band:#044a8a;
  --sky:#1a8fe8;
  --btn:#0a8ff0;
  --text:#555b63;
  --muted:#6b7078;
  --soft:#f8f8f8;
  --line:#8a8f96;
  --placeholder:#dfe2e6;
  --white:#ffffff;
}
*{margin:0;padding:0;box-sizing:border-box}
html,body{width:1200px;height:2609px;overflow:hidden}
body{font-family:'Inter',sans-serif;background:var(--white);position:relative;color:var(--text)}
.abs{position:absolute}
a{text-decoration:none;color:inherit}

.site-header{left:0;top:0;width:1200px;height:100px;background:var(--white);border-bottom:2px solid #d9dadc;box-shadow:0 1px 3px rgba(0,0,0,.12)}
.brand{left:100px;top:34px;font-size:25px;font-weight:700;color:var(--navy);display:flex;align-items:center;gap:10px}
.brand-dot{width:14px;height:14px;border-radius:50%;background:var(--sky)}
.nav{top:39px;font-size:17px;font-weight:500;color:var(--text);white-space:nowrap}
.nav-cta{left:930px;top:24px;width:168px;height:52px;background:var(--btn);color:var(--white);border-radius:4px 26px 26px 4px;font-size:17px;font-weight:600;display:flex;align-items:center;justify-content:center}

.hero{left:0;top:100px;width:1200px;height:604px;background:linear-gradient(90deg,#a9afbd 0%,#c9ccd6 25%,#eeeff2 33%,#e8e9ee 46%,#b7bccb 62%,#cdd1db 80%,#e3e5ea 100%)}
.hero-wash{left:0;top:100px;width:1200px;height:604px;background:rgba(255,255,255,.35)}
.hero-doors{left:895px;top:485px;width:273px;height:195px;background:linear-gradient(90deg,#55545a,#7a3d35 45%,#c9c3c0 70%,#9b6c63);border-radius:3px}
.hero-title{left:0;top:190px;width:1200px;text-align:center;font-size:56px;font-weight:800;color:var(--navy);letter-spacing:-.5px}
.hero-sub{left:0;top:298px;width:1200px;text-align:center;font-size:41px;font-weight:700;color:var(--sky)}
.hero-copy{left:0;top:369px;width:1200px;text-align:center;font-size:16.5px;line-height:26.5px;color:#4a4f57}
.hero-btn{left:506px;top:535px;width:186px;height:60px;background:var(--navy);color:var(--white);font-size:18px;font-weight:600;display:flex;align-items:center;justify-content:center;border-radius:2px;box-shadow:0 2px 4px rgba(0,0,0,.25)}

.feature-band{left:0;top:704px;width:1200px;height:174px;background:var(--band)}
.band-item{top:736px;width:240px;text-align:center;color:var(--white)}
.band-item svg{display:block;margin:0 auto 10px;height:32px}
.band-item h3{font-size:20.5px;font-weight:700;margin-bottom:6px;white-space:nowrap}
.band-item p{font-size:13.5px;line-height:16px}

.products{left:0;top:1028px;width:1200px;height:1254px;background:var(--soft)}
.card-img{top:1040px;height:308px;border-radius:20px}
.card-title{top:1372px;font-size:28px;font-weight:700;color:var(--navy)}
.card-copy{top:1415px;width:260px;font-size:14px;line-height:18.5px;color:var(--muted);white-space:nowrap}
.card-btn{top:1512px;width:86px;height:26px;background:var(--btn);color:var(--white);font-size:10px;font-weight:700;display:flex;align-items:center;justify-content:center;border-radius:2px;box-shadow:0 2px 3px rgba(0,0,0,.2)}

.perk-icon{width:50px;height:42px;background:var(--white);border-radius:6px;box-shadow:0 2px 6px rgba(0,0,0,.15);display:flex;align-items:center;justify-content:center}
.perk-label{font-size:19px;font-weight:600;color:var(--text)}
.enquiry-btn{left:912px;top:1673px;width:186px;height:52px;background:var(--navy);color:var(--white);font-size:17.5px;font-weight:600;display:flex;align-items:center;justify-content:center;border-radius:2px;box-shadow:0 2px 4px rgba(0,0,0,.25)}

.window-img{left:142px;top:1915px;width:222px;height:305px;background:linear-gradient(135deg,#1d1d1f,#3a3b3f 30%,#cfd0d3 50%,#e6e6e8 70%,#1b1b1d);transform:skewY(-4deg);border-radius:4px}
.step{left:608px;width:490px;display:flex;align-items:center;justify-content:space-between}
.step h3{font-size:25.5px;font-weight:700;color:var(--navy)}
.step h3 span{color:var(--sky)}
.step-rule{left:608px;width:490px;height:2px;background:var(--line)}
.step-copy{left:608px;top:2096px;width:500px;font-size:13.5px;line-height:20px;color:var(--text);white-space:nowrap}
.step-btn{left:608px;top:2193px;width:122px;height:34px;background:var(--btn);color:var(--white);font-size:12px;font-weight:700;display:flex;align-items:center;justify-content:center;border-radius:2px}

.footer-rule{left:0;top:2281px;width:1200px;height:3px;background:#8fa3b8}
.footer-brand{left:100px;top:2395px;font-size:31px;font-weight:700;color:var(--navy);display:flex;align-items:center;gap:12px}
.footer-brand .brand-dot{width:18px;height:18px}
.foot-head{font-size:20px;font-weight:700;white-space:nowrap}
.foot-link{font-size:17px;color:var(--text);white-space:nowrap}
.badge{left:950px;top:2368px;width:144px;height:144px;background:var(--placeholder);border-radius:8px}
.legal{left:0;top:2553px;width:1200px;height:37px;background:var(--band);color:var(--white);font-size:13px;display:flex;align-items:center;justify-content:center}
</style>
</head>
<body>

<header class="site-header abs">
  <a class="brand abs" href="#"><span>Corvantek</span><span class="brand-dot"></span></a>
  <a class="nav abs" style="left:507px" href="#">Home</a>
  <a class="nav abs" style="left:596px" href="#">Our Products
    <svg width="11" height="8" viewBox="0 0 11 8"><path d="M1 1.5l4.5 4.5L10 1.5" fill="none" stroke="#0b4a8a" stroke-width="2.2"/></svg></a>
  <a class="nav abs" style="left:740px" href="#">Why Corvantek</a>
  <a class="nav-cta abs" href="#">Make an Enquiry</a>
</header>

<div class="hero abs" role="img" aria-label="Photo of two installers in overalls carrying a white window frame"></div>
<div class="hero-wash abs"></div>
<div class="hero-doors abs" role="img" aria-label="Group of aluminium and timber-look doors and windows"></div>
<h1 class="hero-title abs">Bullet Resistant Window &amp; Doors</h1>
<h2 class="hero-sub abs">Your First Line of Defence</h2>
<p class="hero-copy abs">Lorem Ipsum is simply dummy text of the printing and typesetting industry.<br>Lorem Ipsum has been the industry's. standard dummy text ever since the<br>1500s, when an unknown printer took a galley of type and scrambled it to make a type specimen book.<br>It has survived not only five centuries.</p>
<a class="hero-btn abs" href="#">Learn More</a>

<section class="feature-band abs"></section>
<div class="band-item abs" style="left:207px">
  <svg width="30" height="32" viewBox="0 0 30 32"><path d="M15 1l13 5v9c0 8-6 14-13 16C8 29 2 23 2 15V6z" fill="#fff"/><path d="M9 16l4 4 8-8" fill="none" stroke="#044a8a" stroke-width="3"/></svg>
  <h3>Premium Protection</h3><p>Lorem Ipsum is simply dummy<br>text of the printing Bo</p>
</div>
<div class="band-item abs" style="left:480px">
  <svg width="32" height="32" viewBox="0 0 32 32"><rect x="13" y="0" width="7" height="32" rx="1" transform="rotate(-45 16 16)" fill="#fff"/><path d="M5 5l22 22M27 5L5 27" stroke="#044a8a" stroke-width="2"/><rect x="2" y="2" width="6" height="6" fill="#fff"/><rect x="24" y="24" width="6" height="6" fill="#fff"/></svg>
  <h3>Aesthetically Designed</h3><p>Lorem Ipsum is simply dummy<br>text of the printing Bo</p>
</div>
<div class="band-item abs" style="left:753px">
  <svg width="38" height="32" viewBox="0 0 38 30"><path d="M1 3h22v19H1zM23 9h8l6 7v6H23z" fill="#fff"/><circle cx="8" cy="25" r="4" fill="#fff" stroke="#044a8a" stroke-width="2"/><circle cx="30" cy="25" r="4" fill="#fff" stroke="#044a8a" stroke-width="2"/><path d="M6 12l4 4 7-7" fill="none" stroke="#044a8a" stroke-width="2.5"/></svg>
  <h3>Promptly Delivered</h3><p>Lorem Ipsum is simply dummy<br>text of the printing Bo</p>
</div>

<section class="products abs"></section>
<div class="card-img abs" style="left:100px;width:283px;background:linear-gradient(135deg,#f3f4f8,#dfe3ec 50%,#f7f7fa)" role="img" aria-label="Grey aluminium framed glass door"></div>
<div class="card-img abs" style="left:450px;width:286px;background:linear-gradient(135deg,#f3f4f8,#d9dde6 50%,#f7f7fa)" role="img" aria-label="Black aluminium framed glass door standing open"></div>
<div class="card-img abs" style="left:813px;width:288px;background:linear-gradient(90deg,#5d6f86 0%,#6f8096 35%,#a9c6e6 45%,#d8e7f5 80%,#8fb4de)" role="img" aria-label="Building facade with security camera and reflective glass"></div>

<h3 class="card-title abs" style="left:101px">Product</h3>
<p class="card-copy abs" style="left:101px">Lorem Ipsum is simply dummy<br>text of the printing and typesetting<br>industry. Lorem Ipsum has been the<br>industry's standard...</p>
<a class="card-btn abs" style="left:101px" href="#">Learn more</a>

<h3 class="card-title abs" style="left:451px">Product</h3>
<p class="card-copy abs" style="left:451px">Lorem Ipsum is simply dummy<br>text of the printing and typesetting<br>industry. Lorem Ipsum has been the<br>industry's standard...</p>
<a class="card-btn abs" style="left:451px" href="#">Learn more</a>

<h3 class="card-title abs" style="left:815px">Enquire</h3>
<p class="card-copy abs" style="left:815px">Lorem Ipsum is simply dummy<br>text of the printing and typesetting<br>industry. Lorem Ipsum has been the<br>industry's standard...</p>
<a class="card-btn abs" style="left:815px" href="#">Enquire now</a>

<div class="perk-icon abs" style="left:100px;top:1611px"><svg width="24" height="26" viewBox="0 0 30 32"><path d="M15 1l13 5v9c0 8-6 14-13 16C8 29 2 23 2 15V6z" fill="#0b4a8a"/><path d="M9 16l4 4 8-8" fill="none" stroke="#fff" stroke-width="3"/></svg></div>
<span class="perk-label abs" style="left:170px;top:1621px">Premium Protection</span>
<div class="perk-icon abs" style="left:200px;top:1692px"><svg width="24" height="24" viewBox="0 0 32 32"><rect x="13" y="0" width="7" height="32" rx="1" transform="rotate(-45 16 16)" fill="#0b4a8a"/><path d="M5 5l22 22M27 5L5 27" stroke="#fff" stroke-width="2"/></svg></div>
<span class="perk-label abs" style="left:272px;top:1703px">Aesthetically Designed</span>
<a class="enquiry-btn abs" href="#">Make an Enquiry</a>
<div class="perk-icon abs" style="left:100px;top:1797px"><svg width="30" height="24" viewBox="0 0 38 30"><path d="M1 3h22v19H1zM23 9h8l6 7v6H23z" fill="#0b4a8a"/><circle cx="8" cy="25" r="4" fill="#0b4a8a" stroke="#fff" stroke-width="2"/><circle cx="30" cy="25" r="4" fill="#0b4a8a" stroke="#fff" stroke-width="2"/><path d="M6 12l4 4 7-7" fill="none" stroke="#fff" stroke-width="2.5"/></svg></div>
<span class="perk-label abs" style="left:170px;top:1807px">Promptly Delivered</span>

<div class="window-img abs" role="img" aria-label="Black aluminium window frame with frosted glass"></div>

<div class="step abs" style="top:1893px"><h3><span>01</span> Explore Our Range</h3>
  <svg width="20" height="20" viewBox="0 0 20 20"><circle cx="10" cy="10" r="9.5" fill="#1a8fe8"/><path d="M10 5v10M5 10h10" stroke="#fff" stroke-width="2"/></svg></div>
<div class="step-rule abs" style="top:1946px"></div>
<div class="step abs" style="top:1970px"><h3><span>02</span> Make An Enquiry</h3>
  <svg width="20" height="20" viewBox="0 0 20 20"><circle cx="10" cy="10" r="9.5" fill="#1a8fe8"/><path d="M10 5v10M5 10h10" stroke="#fff" stroke-width="2"/></svg></div>
<div class="step-rule abs" style="top:2023px"></div>
<div class="step abs" style="top:2047px"><h3><span>03</span> Receive Customised Quote</h3>
  <svg width="20" height="20" viewBox="0 0 20 20"><circle cx="10" cy="10" r="9.5" fill="#1a8fe8"/><path d="M5 10h10" stroke="#fff" stroke-width="2"/></svg></div>
<p class="step-copy abs">Lorem Ipsum is simply dummy text of the printing and typesetting industry.<br>Lorem Ipsum has been the industry's standard dummy text ever since the<br>1500s, when an unknown printer took a galley of type and scrambled it to<br>make a type specimen book. It has survived not only five centuries.</p>
<a class="step-btn abs" href="#">Make an Enquiry</a>

<div class="footer-rule abs"></div>
<div class="footer-brand abs"><span>Corvantek</span><span class="brand-dot"></span></div>

<a class="foot-head abs" style="left:408px;top:2313px;color:var(--navy)" href="#">Home</a>
<a class="foot-link abs" style="left:408px;top:2358px" href="#">Why Corvantek</a>
<a class="foot-link abs" style="left:408px;top:2401px" href="#">Make an Enquiry</a>
<a class="foot-link abs" style="left:408px;top:2443px" href="#">Our Products</a>
<a class="foot-link abs" style="left:408px;top:2486px" href="#">Blog</a>

<div class="foot-head abs" style="left:669px;top:2313px;color:var(--sky)">Sydney</div>
<p class="foot-link abs" style="left:669px;top:2358px;line-height:20px">42 Harbour Lane Sydney,<br>NSW 2010 AU</p>
<div class="foot-head abs" style="left:669px;top:2422px;color:var(--navy)">Contact Us</div>
<div class="foot-link abs" style="left:671px;top:2464px;display:flex;gap:10px;align-items:center">
  <svg width="18" height="18" viewBox="0 0 24 24"><path d="M6.6 10.8a15 15 0 006.6 6.6l2.2-2.2c.3-.3.7-.4 1-.2 1.1.4 2.3.6 3.6.6.6 0 1 .4 1 1V20c0 .6-.4 1-1 1A17 17 0 013 4c0-.6.4-1 1-1h3.5c.6 0 1 .4 1 1 0 1.3.2 2.5.6 3.6.1.3 0 .7-.2 1z" fill="#6b7078"/></svg>+61 2000 111 222</div>
<div class="foot-link abs" style="left:671px;top:2502px;display:flex;gap:10px;align-items:center">
  <svg width="18" height="14" viewBox="0 0 18 14"><rect width="18" height="14" fill="#6b7078"/><path d="M0 1l9 7 9-7" fill="none" stroke="#fff" stroke-width="1.6"/></svg>info@corvantek.com</div>

<div class="foot-head abs" style="left:933px;top:2313px;color:var(--text)">Quality Assurance</div>
<div class="badge abs" role="img" aria-label="Quality certification badge"></div>

<footer class="legal abs">Copyright © 2023 -&nbsp; All Rights Reserved by Corvantek</footer>

</body>
</html>
```